Ridgeline Trek Supply - Business Card Design Project

Our company is Ridgeline Trek Supply. We make outdoor gear such as headlamps and flashlights. If you would like to get a feel for our company, feel free to look at our website. www.ridgelinetreksupply.example

And here is my information to put on the card.
Ridgeline Trek Supply
Dana Whitlock
41596 Juniper Hollow Road
Alder Bluff, WA. 97530
support@RidgelineTrekSupply.example
www.RidgelineTrekSupply.example
Facebook.com/RidgelineTrekSupply
Pinterest.com/RidgelineTrekSupply
Twitter.com/RidgelineTrekSupply

Target Market(s)

hunters, campers, preppers

Industry/Entity Type

Sporting Good

Contact Information for Business Card

We would like a card that looks a little outdoorsy. We have 2 logos so one of them should be on the card. The card should also use the colors that are on our logos. The name "Ridgeline Trek Supply" if written out should be in the font "Capture it".

Requirements
Must have
• We currently have 2 logos. At least one must be on the card.
• Must use colors from the logos.
Nice to have
• Possibly a quote from our website. Something like: We don’t just make outdoor gear. We use it. We know it. We live it and we love it.

```html
<!DOCTYPE html>
<html lang="en">
<head>
<meta charset="utf-8">
<title>Ridgeline Trek Supply – Business Card</title>
<link href="https://fonts.googleapis.com/css2?family=Comfortaa:wght@400;700&display=swap" rel="stylesheet">
<style>
  :root {
    --stage: #d9d9d6;
    --ink: #111111;
    --sun-light: #fbe37a;
    --sun-gold: #f2c028;
    --sun-amber: #d8901a;
    --dusk: #7a4a0c;
    --night: #0b0804;
    --accent: #d98a2b;
    --contact: #e3b64a;
  }
  * { box-sizing: border-box; margin: 0; padding: 0; }
  html, body { width: 1200px; height: 900px; overflow: hidden; }
  body {
    background: var(--stage);
    font-family: "Comfortaa", sans-serif;
    position: relative;
  }
  .card {
    position: absolute;
    left: 250px;
    width: 700px;
    height: 400px;
    overflow: hidden;
    box-shadow: 0 10px 28px rgba(0,0,0,.35);
  }
  .card-back { top: 40px; }
  .card-front { top: 460px; }

  .backdrop { position: absolute; inset: 0; }
  .card-back .backdrop {
    background:
      radial-gradient(circle at 78% 42%, #fffbe6 0 4%, var(--sun-light) 12%, var(--sun-gold) 34%, transparent 60%),
      linear-gradient(135deg, var(--dusk) 0%, var(--sun-amber) 35%, var(--sun-gold) 60%, var(--sun-amber) 100%);
  }
  .card-front .backdrop {
    background:
      radial-gradient(ellipse at 70% 30%, var(--sun-light) 0%, transparent 45%),
      linear-gradient(180deg, var(--sun-amber) 0%, var(--sun-gold) 30%, var(--sun-amber) 48%, var(--dusk) 58%, var(--night) 66%, var(--night) 100%);
  }

  .brand {
    position: absolute;
    display: flex;
    align-items: center;
    gap: 12px;
    color: var(--ink);
    font-weight: 700;
    line-height: 1.05;
    white-space: nowrap;
  }
  .brand-mark {
    width: 46px; height: 46px;
    border-radius: 50%;
    background: var(--ink);
    flex: none;
  }
  .card-back .brand { left: 50%; top: 50%; transform: translate(-50%, -50%); font-size: 30px; }
  .card-front .brand { left: 40px; top: 60px; font-size: 26px; }

  .holder-name {
    position: absolute;
    left: 40px; top: 178px;
    font-size: 32px;
    font-weight: 700;
    color: var(--ink);
  }

  .contact {
    position: absolute;
    left: 352px; top: 262px;
    list-style: none;
    color: var(--contact);
    font-size: 13px;
    line-height: 1.5;
  }
  .contact li { display: flex; gap: 10px; align-items: flex-start; margin-bottom: 3px; }
  .contact svg { width: 14px; height: 14px; flex: none; margin-top: 2px; fill: var(--accent); }

  .social {
    position: absolute;
    left: 40px; top: 298px;
  }
  .social-icons { display: flex; gap: 14px; margin-bottom: 10px; }
  .social-icons span {
    width: 28px; height: 28px;
    background: var(--accent);
    border-radius: 3px;
  }
  .social-handle { color: var(--accent); font-size: 15px; }
</style>
</head>
<body>

  <section class="card card-back">
    <div class="backdrop" role="img" aria-label="Golden sunset sky glowing over a mountain ridge"></div>
    <div class="brand"><span class="brand-mark"></span><span class="brand-name">Ridgeline Trek Supply</span></div>
  </section>

  <section class="card card-front">
    <div class="backdrop" role="img" aria-label="Hiker silhouetted against a golden sunset on a dark hilltop"></div>
    <div class="brand"><span class="brand-mark"></span><span class="brand-name">Ridgeline<br>Trek Supply</span></div>
    <h1 class="holder-name">Dana Whitlock</h1>

    <ul class="contact">
      <li><svg viewBox="0 0 16 16"><path d="M8 1 1 7.5h2V15h4v-4h2v4h4V7.5h2z"/></svg><span>www.RidgelineTrekSupply.example</span></li>
      <li><svg viewBox="0 0 16 16"><path d="M1 3h14v10H1z M1 3l7 6 7-6" fill="none" stroke="#d98a2b" stroke-width="1.6"/></svg><span>support@RidgelineTrekSupply.example</span></li>
      <li><svg viewBox="0 0 16 16"><path d="M8 1a5 5 0 0 0-5 5c0 4 5 9 5 9s5-5 5-9a5 5 0 0 0-5-5zm0 7a2 2 0 1 1 0-4 2 2 0 0 1 0 4z"/></svg><span>41596 Juniper Hollow Road<br>Alder Bluff, WA 97530</span></li>
    </ul>

    <div class="social">
      <div class="social-icons"><span></span><span></span><span></span></div>
      <p class="social-handle">/RidgelineTrekSupply</p>
    </div>
  </section>

</body>
</html>
```